Security Consulting Firm needs brochure to be used for advertisement and sales

Need a brochure design for a new security consulting firm based in Metro Detroit called "K. Halvern Security Consulting, LLC" We provide consulting services related to safety and security for our clients. I have attached a file that contains excerpts from our business summary for info to be used (does not have to be word for work or exact), business contact info as well as statistics that i would like added somewhere. I also attached the company logo for use. I would like the logos for Pagemoot, CareerWeft and Snapvane somewhere on the brochure as well. Lastly , I would like the final design to communicate strength, safety, investigation and protection. Thank you
Target Market(s)
Corporate, schools, places of worship, large events, VIP
Industry/Entity Type
Business Consultant
Colors

```html
<!DOCTYPE html>
<html lang="en">
<head>
<meta charset="utf-8">
<title>K. Halvern Security Consulting — Brochure</title>
<link href="https://fonts.googleapis.com/css2?family=Oswald:wght@500;700&family=Open+Sans:wght@400;600;700&display=swap" rel="stylesheet">
<style>
:root{
  --bg:#e9eaec;
  --paper:#ffffff;
  --ink:#1d2733;
  --muted:#5b6672;
  --navy:#0d1e33;
  --blue:#1565b0;
  --sky:#3a9ad9;
  --steel:#2c3a4a;
  --rule:#c9d1da;
}
*{box-sizing:border-box;margin:0;padding:0}
html,body{width:1200px;height:2700px;overflow:hidden;background:var(--bg)}
body{position:relative;font-family:"Open Sans",Arial,sans-serif;color:var(--ink)}
.page{position:absolute;width:550px;height:760px;background:var(--paper);overflow:hidden;box-shadow:0 6px 18px rgba(0,0,0,.12)}
.spread{position:absolute;width:1100px;height:760px;box-shadow:0 8px 22px rgba(0,0,0,.14)}
.spread .page{box-shadow:none}
.title{font-family:"Oswald",Arial,sans-serif;font-weight:700;text-transform:uppercase;letter-spacing:.5px}
.cover-title{position:absolute;left:40px;top:30px;font-size:40px;color:var(--ink)}
.title-rule{position:absolute;left:40px;top:88px;width:470px;height:4px;background:linear-gradient(90deg,var(--blue),var(--sky),transparent)}
.photo{position:absolute}
.photo-cover{left:0;top:108px;width:550px;height:340px;background:linear-gradient(120deg,#0a2747 0%,#1b5e9b 45%,#8fc3e8 75%,#2a4f78 100%)}
.brand{position:absolute;left:36px;top:478px;display:flex;align-items:center;gap:12px}
.brand-dot{width:46px;height:46px;border-radius:50%;background:var(--blue)}
.brand-name{font-family:"Oswald",Arial,sans-serif;font-weight:700;font-size:36px;color:var(--navy);line-height:1}
.brand-sub{position:absolute;left:94px;top:522px;font-size:11px;font-weight:600;color:var(--navy);letter-spacing:1px;text-transform:uppercase}
.cover-copy{position:absolute;left:300px;top:470px;width:220px;font-size:9.5px;line-height:1.5;color:var(--muted)}
.contact-band{position:absolute;left:0;top:600px;width:550px;height:92px;background:linear-gradient(90deg,#ffffff 0%,#ffffff 40%,#dfe7ef 100%)}
.contact-band svg{position:absolute;left:0;top:0}
.contact-list{position:absolute;right:30px;top:18px;list-style:none;font-size:10px;line-height:1.8;color:var(--ink);text-align:right}
.foot{position:absolute;left:0;bottom:0;width:100%;height:68px;background:linear-gradient(180deg,var(--steel),var(--navy));display:flex;align-items:center;justify-content:center;gap:28px}
.social{display:flex;align-items:center;gap:7px;color:#dce6f0;font-size:10.5px;font-weight:600}
.social-dot{width:18px;height:18px;border-radius:50%;background:var(--sky)}
/* back page */
.back-head{position:absolute;left:36px;top:26px;font-size:18px;color:var(--ink)}
.photo-circuit{left:0;top:64px;width:550px;height:320px;background:radial-gradient(circle at 50% 50%,#4fb3ff 0%,#1b5fa8 30%,#0b2a55 70%,#06162f 100%)}
.back-copy{position:absolute;left:36px;top:408px;width:478px;columns:2;column-gap:26px;font-size:9.5px;line-height:1.55;color:var(--muted)}
.back-copy h3{font-family:"Oswald",Arial,sans-serif;font-size:13px;color:var(--ink);margin-bottom:4px;text-transform:uppercase}
.back-copy p{margin-bottom:8px}
.back-contact{position:absolute;left:36px;top:590px;list-style:none;font-size:10px;line-height:1.9;color:var(--ink)}
.back-contact li{display:flex;align-items:center;gap:8px}
.back-contact .pip{width:14px;height:14px;border-radius:3px;background:var(--blue)}
/* inside spread */
.side-panel{position:absolute;left:0;top:0;width:190px;height:692px;background:linear-gradient(180deg,#1c7fcf 0%,#12508f 55%,#0c3461 100%);color:#fff;padding:60px 22px}
.side-title{font-size:30px;line-height:1.05;color:#fff}
.side-rule{width:60px;height:3px;background:#fff;margin:14px 0 16px}
.side-panel p{font-size:9.5px;line-height:1.6;color:#d7e6f5;margin-bottom:10px}
.side-panel ul{list-style:none;font-size:9.5px;line-height:1.8;color:#fff;margin-top:18px}
.photo-strip{left:210px;top:40px;width:620px;height:200px;background:linear-gradient(90deg,#0a213f 0%,#1a4f86 40%,#2f7fc0 60%,#0d2a4e 100%)}
.dark-box{position:absolute;left:850px;top:40px;width:220px;height:230px;background:var(--navy);color:#cfdae6;padding:18px;font-size:9.5px;line-height:1.55}
.dark-box h3{font-family:"Oswald",Arial,sans-serif;font-size:14px;color:#fff;text-transform:uppercase;margin-bottom:8px}
.intro{position:absolute;left:210px;top:262px;width:300px;font-size:9.5px;line-height:1.55;color:var(--muted)}
.services{position:absolute;left:210px;top:330px;width:860px;display:grid;grid-template-columns:1fr 1fr;gap:22px 26px}
.service{border:1px solid var(--rule);padding:14px;background:#f7f9fb}
.service-head{display:flex;align-items:center;gap:10px;margin-bottom:8px}
.service-icon{width:34px;height:34px;flex:none}
.service h4{font-family:"Oswald",Arial,sans-serif;font-weight:500;font-size:13px;text-transform:uppercase;color:var(--ink);line-height:1.2}
.service p{font-size:9.5px;line-height:1.55;color:var(--muted)}
.fold{position:absolute;left:550px;top:0;width:1px;height:100%;background:rgba(0,0,0,.08)}
</style>
</head>
<body>

<!-- Front cover -->
<section class="page front-cover" style="left:325px;top:60px">
  <h1 class="title cover-title">Security Consulting</h1>
  <div class="title-rule"></div>
  <div class="photo photo-cover" role="img" aria-label="Businessman in a suit touching a glowing digital security interface"></div>
  <div class="brand"><span class="brand-dot"></span><span class="brand-name">K. HALVERN</span></div>
  <div class="brand-sub">Security Consulting, LLC</div>
  <p class="cover-copy">Independent safety and security consulting for corporations, schools, places of worship, large events and VIP clients across Metro Detroit. We assess risk, plan response and protect what matters most.</p>
  <div class="contact-band">
    <svg width="550" height="92" viewBox="0 0 550 92"><polygon points="0,0 230,0 190,92 0,92" fill="#1565b0"/><polygon points="230,0 250,0 210,92 190,92" fill="#3a9ad9"/></svg>
    <ul class="contact-list"><li>(248) 555-0142</li><li>info@khalvernsecurity.com</li><li>www.khalvernsecurity.com</li></ul>
  </div>
  <footer class="foot">
    <span class="social"><span class="social-dot"></span>Pagemoot</span>
    <span class="social"><span class="social-dot"></span>CareerWeft</span>
    <span class="social"><span class="social-dot"></span>Snapvane</span>
  </footer>
</section>

<!-- Outer spread: back + front -->
<section class="spread outer-spread" style="left:50px;top:920px">
  <div class="page back-page" style="left:0;top:0">
    <h2 class="title back-head">Keep pace with evolving risk</h2>
    <div class="photo photo-circuit" role="img" aria-label="Blue circuit board with a glowing padlock at its centre"></div>
    <div class="back-copy">
      <h3>Who we are</h3>
      <p>We are a veteran-led team with years of field experience in law enforcement, investigations and protective operations.</p>
      <p>Our mission is to help every client build a safer place to work, learn, worship and gather.</p>
      <h3>Why it matters</h3>
      <p>Threats change quickly. A clear plan, trained people and tested procedures reduce harm and speed recovery.</p>
    </div>
    <ul class="back-contact">
      <li><span class="pip"></span>(248) 555-0142</li>
      <li><span class="pip"></span>info@khalvernsecurity.com</li>
      <li><span class="pip"></span>Metro Detroit, Michigan</li>
    </ul>
    <footer class="foot">
      <span class="social"><span class="social-dot"></span>Pagemoot</span>
      <span class="social"><span class="social-dot"></span>CareerWeft</span>
      <span class="social"><span class="social-dot"></span>Snapvane</span>
    </footer>
  </div>
  <div class="page front-page" style="left:550px;top:0">
    <h1 class="title cover-title">Security Consulting</h1>
    <div class="title-rule"></div>
    <div class="photo photo-cover" role="img" aria-label="Businessman in a suit touching a glowing digital security interface"></div>
    <div class="brand"><span class="brand-dot"></span><span class="brand-name">K. HALVERN</span></div>
    <div class="brand-sub">Security Consulting, LLC</div>
    <p class="cover-copy">Independent safety and security consulting for corporations, schools, places of worship, large events and VIP clients across Metro Detroit. We assess risk, plan response and protect what matters most.</p>
    <div class="contact-band">
      <svg width="550" height="92" viewBox="0 0 550 92"><polygon points="0,0 230,0 190,92 0,92" fill="#1565b0"/><polygon points="230,0 250,0 210,92 190,92" fill="#3a9ad9"/></svg>
      <ul class="contact-list"><li>(248) 555-0142</li><li>info@khalvernsecurity.com</li><li>www.khalvernsecurity.com</li></ul>
    </div>
    <footer class="foot">
      <span class="social"><span class="social-dot"></span>Pagemoot</span>
      <span class="social"><span class="social-dot"></span>CareerWeft</span>
      <span class="social"><span class="social-dot"></span>Snapvane</span>
    </footer>
  </div>
  <div class="fold"></div>
</section>

<!-- Inside spread -->
<section class="spread inside-spread" style="left:50px;top:1840px">
  <div class="page" style="left:0;top:0;width:1100px">
    <aside class="side-panel">
      <h2 class="title side-title">Security<br>Consulting</h2>
      <div class="side-rule"></div>
      <p>K. Halvern Security Consulting, LLC provides practical safety and security guidance built on real field experience.</p>
      <p>We work side by side with leaders to find gaps, train staff and prepare for the unexpected.</p>
      <ul><li>• Corporate</li><li>• Schools</li><li>• Places of worship</li><li>• Large events</li><li>• VIP</li></ul>
    </aside>
    <div class="photo photo-strip" role="img" aria-label="Digital security icons floating over a dark blue technology background"></div>
    <div class="dark-box">
      <h3>Our approach</h3>
      <p>Every engagement begins with listening. We study your site, people and daily routines, then deliver a clear written plan with priorities you can act on right away.</p>
    </div>
    <p class="intro">Our services are tailored to the size and needs of each client, from a single building to a multi-day public event.</p>
    <div class="services">
      <article class="service">
        <div class="service-head"><svg class="service-icon" viewBox="0 0 34 34"><rect width="34" height="34" rx="4" fill="#1565b0"/><circle cx="15" cy="15" r="7" fill="none" stroke="#fff" stroke-width="2.5"/><line x1="20" y1="20" x2="27" y2="27" stroke="#fff" stroke-width="3"/></svg><h4>Vulnerability Assessment</h4></div>
        <p>On-site review of access points, lighting, cameras and procedures, with ranked recommendations.</p>
      </article>
      <article class="service">
        <div class="service-head"><svg class="service-icon" viewBox="0 0 34 34"><rect width="34" height="34" rx="4" fill="#1565b0"/><path d="M17 7 L27 26 H7 Z" fill="none" stroke="#fff" stroke-width="2.5"/><line x1="17" y1="14" x2="17" y2="20" stroke="#fff" stroke-width="2.5"/></svg><h4>Threat Assessment &amp; Management</h4></div>
        <p>Structured review of concerning behaviour and a team plan to reduce risk early.</p>
      </article>
      <article class="service">
        <div class="service-head"><svg class="service-icon" viewBox="0 0 34 34"><rect width="34" height="34" rx="4" fill="#1565b0"/><path d="M9 18 L15 24 L26 11" fill="none" stroke="#fff" stroke-width="3"/></svg><h4>Emergency Planning &amp; Training</h4></div>
        <p>Written response plans, staff drills and tabletop exercises that build confidence.</p>
      </article>
      <article class="service">
        <div class="service-head"><svg class="service-icon" viewBox="0 0 34 34"><rect width="34" height="34" rx="4" fill="#1565b0"/><path d="M17 6 L26 10 V17 C26 23 22 27 17 29 C12 27 8 23 8 17 V10 Z" fill="none" stroke="#fff" stroke-width="2.5"/></svg><h4>Personal Protection</h4></div>
        <p>Discreet protective planning for executives, guests and high-profile visitors.</p>
      </article>
    </div>
    <footer class="foot">
      <span class="social"><span class="social-dot"></span>Pagemoot</span>
      <span class="social"><span class="social-dot"></span>CareerWeft</span>
      <span class="social"><span class="social-dot"></span>Snapvane</span>
    </footer>
  </div>
  <div class="fold"></div>
</section>

</body>
</html>
```